Classic Minimalistic Business Card

Design a classic, minimalistic Business Card. Please find inspiration in the attached Classic Minimalistic examples. My information:
Name: Glen Ovamir
Company: Ovamir Capital
Logo: OC
Address: 1470 N Thornwick Rd, Suite 210 | Geneva, IL 60134
Phone: 630-555-0192
Email: glenovamir@pvt.insure
Slogan: Building Strength Through Capital

Feel free to leave out any of the information above except my name.

I have selected Double-sided, but I am also open to Single-sided

Target Market(s)

22-70. income greater than 150k/year

Industry/Entity Type

Finance

Contact Information for Business Card

See Project Description

Requirements
Must have
• Ivory or "antiqued" background similar to the reference pictures

```html
<!DOCTYPE html>
<html lang="en">
<head>
<meta charset="utf-8">
<title>Ovamir Capital — Business Card</title>
<link rel="stylesheet" href="https://fonts.googleapis.com/css2?family=Antic+Didone&family=Parisienne&display=swap">
<style>
  :root {
    --backdrop: #1c1c1c;
    --backdrop-glow: #2e2e2e;
    --ivory: #fdfeee;
    --ink: #1a1a1a;
  }
  html, body {
    margin: 0;
    padding: 0;
    width: 1200px;
    height: 470px;
    overflow: hidden;
  }
  body {
    background: radial-gradient(ellipse at center, var(--backdrop-glow) 0%, var(--backdrop) 75%);
    position: relative;
    font-family: "Antic Didone", serif;
    color: var(--ink);
  }
  .card {
    position: absolute;
    top: 100px;
    width: 474px;
    height: 270px;
    background: var(--ivory);
  }
  .card--front { left: 95px; }
  .card--back { left: 631px; }

  .card__name {
    position: absolute;
    left: 0;
    right: 0;
    top: 98px;
    margin: 0;
    text-align: center;
    font-weight: 400;
    font-size: 52px;
    line-height: 1;
    letter-spacing: 0.02em;
    text-transform: uppercase;
    transform: scaleX(0.58);
    transform-origin: center;
  }
  .card__tagline {
    position: absolute;
    left: 0;
    right: 0;
    top: 163px;
    margin: 0;
    text-align: center;
    font-family: "Parisienne", cursive;
    font-size: 14px;
    line-height: 1;
  }
  .card__footer {
    position: absolute;
    left: 25px;
    right: 26px;
    top: 236px;
    display: flex;
    justify-content: space-between;
    font-size: 11px;
    line-height: 1;
  }
  .card__company,
  .card__address {
    display: inline-block;
    transform: scaleX(0.72);
  }
  .card__company { transform-origin: left center; }
  .card__address { transform-origin: right center; white-space: nowrap; }

  .card__phone {
    position: absolute;
    left: 0;
    right: 0;
    top: 112px;
    margin: 0;
    text-align: center;
    font-size: 48px;
    line-height: 1;
    transform: scaleX(0.62);
    transform-origin: center;
    white-space: nowrap;
  }
  .card__phone-dash {
    display: inline-block;
    width: 24px;
    height: 5px;
    background: var(--ink);
    vertical-align: middle;
    margin: 0 10px 6px;
  }
</style>
</head>
<body>
  <section class="card card--front" aria-label="Card front">
    <h1 class="card__name">Glen Ovamir</h1>
    <p class="card__tagline">Building Strength Through Capital</p>
    <div class="card__footer">
      <span class="card__company">Ovamir Capital</span>
      <span class="card__address">1470 N Thornwick Rd, Suite 210 | Geneva, IL 60134</span>
    </div>
  </section>

  <section class="card card--back" aria-label="Card back">
    <p class="card__phone" aria-label="630-555-0192">630<span class="card__phone-dash"></span>555<span class="card__phone-dash"></span>0192</p>
  </section>
</body>
</html>
```